Flyer for Beach Exercise Programme

Hi,
We need an E-Flyer (International Paper A5 size) for an upcoming classes we are running starting on 7th April. The classes will happen every monday and wednesday at 6am and will be on the beach. The exercises will be called Feral by the shore and comprise of the activities in the pictures. You can feel free to take pictures from our instagram profile (@corvashore) or website/facebook (www.corvashore.ae - www.facebook.com/corvashore) for this project.
We need the flyer to be WOW, edgy design incorporating elements that make people looking at it think it would be amazing to work out at a beach and look at the sea. The logos of both companies (Corva Shore & Brimley Gym) should be included in the flyer and the blurb should read:
Feral by the Shore
Non Members - 100AED
Members - Free
I also want to promote ours and Brimley instagram/facebook/website so if you can make a dual theme to the flyer so that one half is for corva shore, the other half is for brimley gym - the gym who supplied the photos enclosed, and like the the two entities are coming together in a way to create these special classes.
Our contact details are as follows:
info@corvashore.ae
instagram (use the logo) @corvashore
twitter (use the logo) @corvashore
facebook (use the logo) facebook.com/corvashore
Brimley contact info is as follows:
info@brimleygym.example
instagram @brimley
twitter @brimley
facebook.com/brimley
Please if you can also make a cropped version that we can use as our facebook banner that would be awesome (851x351 pixels)

```html
<!DOCTYPE html>
<html lang="en">
<head>
<meta charset="utf-8">
<title>Feral by the Shore</title>
<link rel="stylesheet" href="https://fonts.googleapis.com/css2?family=Arvo:wght@700&family=Montserrat:wght@400;500;700;800&display=swap">
<style>
  :root {
    --navy: #0f3445;
    --maroon: #8a1c4a;
    --pink: #e8717f;
    --plum: #6a2a6e;
    --teal: #2c6577;
    --slate: #3b4a58;
    --rule: #cfc9c2;
    --paper: #ffffff;
    --mail-red: #d8334a;
    --icon-grey: #5b6b78;
  }
  html, body {
    margin: 0;
    padding: 0;
    overflow: hidden;
    background: #e9e9e9;
  }
  .flyer {
    position: relative;
    width: 850px;
    height: 1200px;
    overflow: hidden;
    background: var(--paper);
    font-family: "Montserrat", Arial, sans-serif;
  }
  .hero-photo {
    position: absolute;
    left: 0; top: 0;
    width: 850px; height: 447px;
    background: linear-gradient(180deg,
      #6f8592 0%, #9fb2bb 28%, #c9d6d9 40%,
      #7fb9bd 46%, #5fa5ab 54%, #8cc3c2 60%,
      #e9e6df 66%, #f4f1ea 82%, #ddd7cd 100%);
  }
  .navy-sweep {
    position: absolute;
    left: 0; top: 0;
    width: 850px; height: 1200px;
  }
  .title {
    position: absolute;
    left: 42px;
    margin: 0;
    white-space: nowrap;
  }
  .title-lead {
    top: 498px;
    font-family: "Montserrat", Arial, sans-serif;
    font-weight: 800;
    font-size: 50px;
    letter-spacing: 1px;
    color: var(--maroon);
  }
  .title-main {
    top: 548px;
    font-family: "Arvo", Georgia, serif;
    font-weight: 700;
    font-size: 132px;
    line-height: 1;
    letter-spacing: 2px;
    color: var(--navy);
  }
  .schedule {
    position: absolute;
    left: 42px; top: 692px;
    white-space: nowrap;
  }
  .schedule p { margin: 0; }
  .schedule .from {
    font-size: 22px; font-weight: 500; color: var(--pink); line-height: 1.2;
  }
  .schedule .date {
    font-size: 31px; font-weight: 800; color: var(--maroon); line-height: 1.2;
  }
  .schedule .days {
    font-size: 19px; font-weight: 700; color: var(--maroon); line-height: 1.35;
  }
  .schedule .price-members {
    margin-top: 30px;
    font-size: 21px; font-weight: 500; color: var(--pink); line-height: 1.3;
  }
  .schedule .price-guests {
    font-size: 21px; font-weight: 500; color: var(--plum); line-height: 1.3;
  }
  .divider-v {
    position: absolute;
    width: 2px;
    background: var(--rule);
  }
  .divider-schedule { left: 352px; top: 695px; height: 215px; }
  .organizers {
    position: absolute;
    left: 382px; top: 746px;
    white-space: nowrap;
  }
  .organizers h2 {
    margin: 0 0 22px;
    font-size: 23px; font-weight: 700; color: var(--teal);
  }
  .partner-marks {
    display: flex;
    gap: 26px;
    align-items: center;
  }
  .partner-name {
    display: flex;
    align-items: center;
    gap: 8px;
    font-size: 18px; font-weight: 700; color: var(--teal);
  }
  .partner-dot {
    width: 14px; height: 14px; border-radius: 50%;
    background: var(--teal);
  }
  .contact-heading {
    position: absolute;
    left: 42px; top: 994px;
    margin: 0;
    font-size: 22px; font-weight: 700; color: var(--slate);
  }
  .contact-list {
    position: absolute;
    top: 1034px;
    margin: 0; padding: 0;
    list-style: none;
    white-space: nowrap;
  }
  .contact-list li {
    display: flex;
    align-items: center;
    gap: 7px;
    height: 23px;
    font-size: 15px; font-weight: 500; color: var(--slate);
  }
  .contact-host { left: 42px; }
  .contact-partner { left: 306px; }
  .divider-contact { left: 282px; top: 1028px; height: 150px; }
  .icon-mail { width: 16px; height: 12px; flex: none; }
  .icon-social {
    width: 12px; height: 12px; flex: none;
    background: var(--icon-grey); border-radius: 2px;
  }
</style>
</head>
<body>
<main class="flyer">
  <div class="hero-photo" role="img" aria-label="Photo of a trainer leading a group doing leg-raise exercises on mats on a white sand beach by the sea"></div>

  <svg class="navy-sweep" viewBox="0 0 850 1200" aria-hidden="true">
    <path d="M530,447 L850,447 L850,1200 L280,1200 C680,1160 840,1060 830,790 C830,610 710,475 530,447 Z" fill="var(--navy)"/>
  </svg>

  <h1 class="title title-lead">Feral by the</h1>
  <p class="title title-main">Shore</p>

  <section class="schedule">
    <p class="from">Starting from</p>
    <p class="date">7th April 2014</p>
    <p class="days">MONDAY &amp; WEDNESDAY<br>at 6am</p>
    <p class="price-members">Members - Free</p>
    <p class="price-guests">Non Members - 100AED</p>
  </section>
  <div class="divider-v divider-schedule"></div>

  <section class="organizers">
    <h2>Organized by:</h2>
    <div class="partner-marks">
      <span class="partner-name"><span class="partner-dot"></span>Corva Shore</span>
      <span class="partner-name">Brimley Gym</span>
    </div>
  </section>

  <h2 class="contact-heading">Contact:</h2>
  <ul class="contact-list contact-host">
    <li><svg class="icon-mail" viewBox="0 0 18 13"><rect x="0.75" y="0.75" width="16.5" height="11.5" fill="none" stroke="var(--mail-red)" stroke-width="1.5"/><path d="M1 1 L9 7.5 L17 1" fill="none" stroke="var(--mail-red)" stroke-width="1.5"/></svg>info@corvashore.ae</li>
    <li><span class="icon-social"></span>instagram@corvashore</li>
    <li><span class="icon-social"></span>twitter@corvashore</li>
    <li><span class="icon-social"></span>facebook.com/corvashore</li>
  </ul>
  <div class="divider-v divider-contact"></div>
  <ul class="contact-list contact-partner">
    <li><svg class="icon-mail" viewBox="0 0 18 13"><rect x="0.75" y="0.75" width="16.5" height="11.5" fill="none" stroke="var(--mail-red)" stroke-width="1.5"/><path d="M1 1 L9 7.5 L17 1" fill="none" stroke="var(--mail-red)" stroke-width="1.5"/></svg>info@brimleygym.example</li>
    <li><span class="icon-social"></span>instagram@brimley</li>
    <li><span class="icon-social"></span>twitter@brimley</li>
    <li><span class="icon-social"></span>facebook.com/brimley</li>
  </ul>
</main>
</body>
</html>
```